“We’re Hiring” Canva Template for LinkedIn Posts

We’re looking for a modern, eye-catching LinkedIn post template that we can easily reuse whenever we announce new job openings.
The final design must be editable in Canva so that our marketing team can update the position title, location, and hiring manager information for future hires.

Key Requirements:
Format: Canva Template (editable)
Primary Logo: ORLA Graft KT
Secondary Logo: Tarrow Biologics (can appear smaller, e.g., bottom corner)
Headline Options: “We’re Hiring” or “Join Our Team”

Editable Text Fields:
Job Title
Location (City / State)
Hiring Manager’s Name
Hiring Manager’s Email (with clear direction such as “Email [Name] at [Email] to apply”)

Design Style:
Tone: Professional, clean, and modern
Color Palette: Use ORLA Graft KT brand colors prominently (Tarrow secondary accent is fine)
Layout: Easy to read at a glance when scrolling LinkedIn
Aesthetic Keywords: Polished, credible, corporate, but visually appealing
Font Style: Clean sans-serif fonts preferred (modern and readable)

Design Inspiration:
We’d like something that feels in line with modern biotech/medical device marketing—professional but visually sharp. Examples include layouts with:
A hero headline at the top (“We’re Hiring” / “Join Our Team”)
Company logo lockup with hierarchy (ORLA Graft KT primary, Tarrow secondary)
A clear call-to-action section for the hiring manager’s contact
Optional background texture or subtle gradient using brand colors

Usage:
This template will be used primarily for LinkedIn and other professional social media posts, so designs should be optimized for 1920 x 1080 pixels (portrait) or 1080 x 1080 pixels (square).

```html
<!DOCTYPE html>
<html lang="en">
<head>
<meta charset="utf-8">
<title>We Are Hiring – ORLA Graft KT</title>
<link rel="stylesheet" href="https://fonts.googleapis.com/css2?family=League+Spartan:wght@500;600;700;800&display=swap">
<style>
  :root {
    --plum: #7b1a7a;
    --plum-soft: #c9a0cc;
    --magenta: #c83aa6;
    --lime: #9dcb5e;
    --lime-soft: #cfe3bd;
    --ink: #0b0b0b;
    --white: #ffffff;
    --brand: #8a2480;
  }
  * { margin: 0; padding: 0; box-sizing: border-box; }
  html, body { width: 1200px; height: 1200px; overflow: hidden; background: var(--white); }
  body { font-family: "League Spartan", "Helvetica Neue", Arial, sans-serif; }

  .post {
    position: relative;
    width: 1200px;
    height: 1200px;
    overflow: hidden;
    background: var(--white);
  }
  .backdrop {
    position: absolute;
    inset: 0;
    background:
      radial-gradient(ellipse 620px 520px at 1140px 80px, rgba(176,120,184,0.85), rgba(201,160,204,0.45) 55%, rgba(255,255,255,0) 80%),
      radial-gradient(ellipse 760px 720px at -40px 1200px, rgba(170,208,140,0.75), rgba(207,227,189,0.5) 55%, rgba(255,255,255,0) 85%);
  }
  .texture {
    position: absolute;
    right: 0;
    top: 0;
    width: 560px;
    height: 560px;
    background: radial-gradient(circle at 70% 40%, rgba(140,140,160,0.12), rgba(255,255,255,0) 70%);
  }
  .texture--low {
    right: auto;
    top: auto;
    left: 0;
    bottom: 0;
    width: 820px;
    height: 360px;
    background: radial-gradient(ellipse at 40% 70%, rgba(120,150,110,0.14), rgba(255,255,255,0) 70%);
  }

  .brand-primary {
    position: absolute;
    left: 87px;
    top: 70px;
    font-size: 50px;
    font-weight: 700;
    letter-spacing: -0.5px;
    color: var(--brand);
  }
  .brand-secondary {
    position: absolute;
    right: 95px;
    top: 76px;
    font-size: 36px;
    font-weight: 600;
    color: var(--white);
  }

  .headline {
    position: absolute;
    left: 128px;
    top: 172px;
    color: var(--ink);
    font-weight: 700;
  }
  .headline__lead {
    display: block;
    font-size: 142px;
    line-height: 1;
    letter-spacing: -2px;
  }
  .headline__main {
    display: block;
    font-size: 268px;
    line-height: 0.9;
    letter-spacing: -5px;
    margin-top: 2px;
  }

  .contact-panel {
    position: absolute;
    left: 78px;
    top: 550px;
    width: 1058px;
    height: 481px;
    border-radius: 46px;
    background: var(--plum);
  }
  .role-tag {
    position: absolute;
    left: 81px;
    top: 50px;
    width: 358px;
    height: 86px;
    border-radius: 43px;
    background: var(--white);
    color: var(--ink);
    font-size: 38px;
    font-weight: 700;
    display: flex;
    align-items: center;
    justify-content: center;
    padding-top: 4px;
  }
  .role-title {
    position: absolute;
    left: 0;
    width: 520px;
    top: 164px;
    text-align: center;
    color: var(--lime);
    font-size: 43px;
    font-weight: 700;
  }
  .location {
    position: absolute;
    left: 66px;
    top: 292px;
    font-weight: 700;
  }
  .location__label { color: var(--white); font-size: 34px; line-height: 1.25; }
  .location__value { color: var(--lime); font-size: 35px; line-height: 1.2; }

  .divider {
    position: absolute;
    left: 509px;
    top: 52px;
    width: 20px;
    height: 380px;
  }

  .cta {
    position: absolute;
    left: 557px;
    top: 40px;
  }
  .cta__heading {
    color: var(--white);
    font-size: 76px;
    font-weight: 700;
    line-height: 0.98;
    letter-spacing: -0.5px;
  }
  .cta__name {
    margin-top: 30px;
    color: var(--lime);
    font-size: 50px;
    font-weight: 700;
  }
  .cta__email {
    display: inline-block;
    margin-top: 14px;
    margin-left: 8px;
    color: var(--white);
    font-size: 33px;
    font-weight: 500;
    text-decoration: underline;
    text-underline-offset: 4px;
    text-decoration-thickness: 2px;
  }

  .apply-button {
    position: absolute;
    left: 637px;
    top: 958px;
    width: 474px;
    height: 125px;
    border-radius: 62px;
    background: var(--lime);
    color: var(--plum);
    font-size: 60px;
    font-weight: 700;
    display: flex;
    align-items: center;
    justify-content: center;
    padding-top: 6px;
    letter-spacing: -0.5px;
  }
</style>
</head>
<body>
  <main class="post">
    <div class="backdrop"></div>
    <div class="texture" role="img" aria-label="Faint grey hexagon molecular pattern"></div>
    <div class="texture texture--low" role="img" aria-label="Faint green hexagon molecular pattern"></div>

    <div class="brand-primary">ORLA Graft KT</div>
    <div class="brand-secondary">Tarrow</div>

    <h1 class="headline">
      <span class="headline__lead">We Are</span>
      <span class="headline__main">Hiring!</span>
    </h1>

    <section class="contact-panel">
      <div class="role-tag">OPEN POSITION</div>
      <div class="role-title">BioMedical Engineer</div>
      <div class="location">
        <div class="location__label">LOCATION:</div>
        <div class="location__value">Ridgeview Park 4, Alder St.</div>
        <div class="location__value">Colorado, USA</div>
      </div>

      <svg class="divider" viewBox="0 0 20 380" aria-hidden="true">
        <line x1="10" y1="12" x2="10" y2="368" stroke="#c83aa6" stroke-width="3"/>
        <circle cx="10" cy="10" r="7" fill="none" stroke="#c83aa6" stroke-width="3"/>
        <circle cx="10" cy="370" r="7" fill="none" stroke="#c83aa6" stroke-width="3"/>
      </svg>

      <div class="cta">
        <div class="cta__heading">Send your<br>Resume to</div>
        <div class="cta__name">Maren T. Doyle</div>
        <a class="cta__email">marentdoyle@orlagraft.com</a>
      </div>
    </section>

    <div class="apply-button">APPLY NOW!</div>
  </main>
</body>
</html>
```